Need 4 childhood cancer facts posters

Hello. I run a nonprofit in East Tennessee, USA that supports children with cancer and their families.

I need 4 poster designs with facts about childhood cancers. It should either have pictures of children with cancer or be focused around the whole idea of childhood cancer awareness. This project will require time and research. I will post links to facts as the project goes forward.

Questions can be emailed to tmerrow@glowwithnora.org. AI format of our logo has been uploaded. I have images and links here http://www.glowwithnora.org/contest-pics.html

You can also view our website at www.glowwithnora.org

Some facts: http://pelt.tumorstats.example/archive/publications/childhood/

USE THESE FACTS: * Everyday, approximately 250 children will die from childhood cancer. *Childhood Cancers is the number 1 cause of death in children under age 15 in the US. *Less than 5% of the federal governments budget toward cancer research is dedicated to childhood cancers. *One in 330 children will be diagnosed with cancer by the time they are 20.

Poster will be 24 inches wide by 36 inches tall.

```html
<!DOCTYPE html>
<html lang="en">
<head>
<meta charset="utf-8">
<title>Childhood Cancer Facts Posters</title>
<link rel="stylesheet" href="https://fonts.googleapis.com/css2?family=Ubuntu:wght@400;500&family=Dancing+Script:wght@700&display=swap">
<style>
  :root {
    --yellow-light: #ffd21a;
    --yellow-deep: #f2a900;
    --ink: #111111;
    --grey-text: #555555;
    --gutter: #ffffff;
    --frame: #222222;
  }
  * { box-sizing: border-box; margin: 0; padding: 0; }
  html, body { width: 1200px; height: 410px; overflow: hidden; background: var(--gutter); }
  .poster-series { position: relative; width: 1200px; height: 410px; }
  .poster {
    position: absolute; top: 0; width: 291px; height: 410px; overflow: hidden;
    font-family: "Ubuntu", sans-serif; color: var(--ink);
  }
  .poster:nth-child(2) { left: 0; }
  .poster:nth-child(3) { left: 303px; }
  .poster:nth-child(4) { left: 606px; }
  .poster:nth-child(5) { left: 909px; }
  .poster__art { position: absolute; inset: 0; width: 291px; height: 410px; }
  .shared-defs { position: absolute; width: 0; height: 0; }

  .yellow-sweep { fill: url(#yellowGrad); stroke: #fff; stroke-width: 4; }
  .lower-sheet { fill: url(#sheetGrad); stroke: #fff; stroke-width: 4; }
  .ribbon-drop { fill: #fff; }
  .portrait-card { fill: url(#monoGrad); stroke: #fff; stroke-width: 5; }
  .brand-pill { fill: url(#yellowGrad); }
  .support-frame { fill: none; stroke: var(--frame); stroke-width: 2; }

  .poster--losses .photo-hero { fill: url(#mudGrad); }
  .poster--cause .photo-hero { fill: url(#earthGrad); }
  .poster--funding .photo-hero { fill: url(#cellGrad); }
  .poster--odds .photo-hero { fill: url(#wardGrad); }

  .headline {
    position: absolute; left: 34px; top: 52px;
    font-weight: 500; font-size: 21px; line-height: 25px; letter-spacing: -0.2px;
  }
  .fact-label {
    position: absolute; left: 34px; top: 160px; width: 100px;
    display: flex; align-items: center; gap: 5px; font-size: 6.5px;
  }
  .fact-label::before, .fact-label::after {
    content: ""; flex: 1; height: 1px; background: var(--ink);
  }
  .fact-title {
    position: absolute; left: 34px; top: 170px; white-space: nowrap;
    font-family: "Dancing Script", cursive; font-size: 15px; line-height: 20px; font-weight: 700;
  }
  .fact-stat {
    position: absolute; left: 34px; top: 194px; width: 122px;
    font-size: 7px; line-height: 9px; font-weight: 400;
  }
  .support-note {
    position: absolute; left: 26px; top: 320px; width: 70px;
    font-size: 4.8px; line-height: 6px; font-weight: 500; text-transform: uppercase;
  }
  .brand {
    position: absolute; left: 150px; top: 310px; width: 135px;
    display: flex; align-items: flex-start; gap: 5px;
  }
  .brand__dot { width: 7px; height: 7px; border-radius: 50%; background: var(--yellow-light); margin-top: 3px; flex: none; }
  .brand__name { font-size: 9px; line-height: 10px; color: var(--grey-text); font-weight: 400; }
  .contact-email {
    position: absolute; left: 130px; top: 378px; width: 161px; text-align: center;
    font-size: 6.5px; color: var(--grey-text);
  }
  .site-url {
    position: absolute; left: 130px; top: 396px; width: 161px; text-align: center;
    font-size: 8.5px; font-weight: 500; letter-spacing: 0.3px; color: var(--ink);
  }
</style>
</head>
<body>
<main class="poster-series">
  <svg class="shared-defs" aria-hidden="true">
    <defs>
      <linearGradient id="yellowGrad" x1="0" y1="0" x2="1" y2="1">
        <stop offset="0" stop-color="#ffd21a"/><stop offset="1" stop-color="#f2a900"/>
      </linearGradient>
      <linearGradient id="sheetGrad" x1="0" y1="0" x2="0" y2="1">
        <stop offset="0" stop-color="#ffffff"/><stop offset="1" stop-color="#e4e4e4"/>
      </linearGradient>
      <linearGradient id="monoGrad" x1="0" y1="0" x2="1" y2="1">
        <stop offset="0" stop-color="#cfcfcf"/><stop offset="1" stop-color="#4a4a4a"/>
      </linearGradient>
      <linearGradient id="mudGrad" x1="0" y1="0" x2="0" y2="1">
        <stop offset="0" stop-color="#5b4e44"/><stop offset="1" stop-color="#a39486"/>
      </linearGradient>
      <linearGradient id="earthGrad" x1="0" y1="0" x2="1" y2="1">
        <stop offset="0" stop-color="#8a5a3a"/><stop offset="1" stop-color="#b99a78"/>
      </linearGradient>
      <radialGradient id="cellGrad" cx="0.6" cy="0.4" r="0.8">
        <stop offset="0" stop-color="#8a2f32"/><stop offset="1" stop-color="#3b0f14"/>
      </radialGradient>
      <linearGradient id="wardGrad" x1="0" y1="0" x2="0" y2="1">
        <stop offset="0" stop-color="#d8cfc5"/><stop offset="1" stop-color="#a79c92"/>
      </linearGradient>
    </defs>
  </svg>

  <article class="poster poster--losses">
    <svg class="poster__art" viewBox="0 0 291 410">
      <rect class="photo-hero" x="110" y="0" width="181" height="300" role="img" aria-label="Photo: heavy boot stepping on crayons in mud"/>
      <path class="yellow-sweep" d="M-4,-4 H142 C112,70 150,150 210,180 C245,198 291,205 295,215 V310 H-4Z"/>
      <path class="lower-sheet" d="M-4,320 C90,255 200,236 295,262 V414 H-4Z"/>
      <path class="ribbon-drop" d="M228,132 C208,102 192,80 192,50 A36,36 0 0 1 264,50 C264,80 248,102 228,132Z"/>
      <path class="portrait-card" role="img" aria-label="Black and white photo of a child with cancer" d="M80,300 C64,300 60,286 68,274 L100,236 C108,228 118,226 130,226 H204 C222,226 228,240 218,254 L188,290 C180,298 170,300 158,300Z"/>
      <path class="support-frame" d="M22,332 V318 H36 M90,346 V360 H76"/>
      <g><rect x="24" y="350" width="13" height="8" rx="1" fill="#e8412c"/><rect x="39" y="350" width="13" height="8" rx="1" fill="#1a3a8f"/><rect x="54" y="350" width="13" height="8" rx="1" fill="#2e8bd6"/><rect x="69" y="350" width="13" height="8" rx="1" fill="#f08a1c"/></g>
      <circle cx="210" cy="362" r="2.5" fill="#333"/><rect x="205" y="367" width="5" height="5" fill="#333"/><rect x="212" y="367" width="5" height="5" fill="#333"/>
      <path class="brand-pill" d="M140,392 H295 V414 H130 C130,400 134,392 140,392Z"/>
    </svg>
    <h2 class="headline">DONATE<br>today<br>to HELP<br>a CHILD!</h2>
    <p class="fact-label">Fact 1</p>
    <p class="fact-title">Daily Losses</p>
    <p class="fact-stat">Every day, approximately 250 children die from childhood cancer.</p>
    <p class="support-note">Show your support with a small contribution today!</p>
    <div class="brand"><span class="brand__dot"></span><p class="brand__name">Nora Whitfield<br>Childhood Cancer Foundation</p></div>
    <p class="contact-email">foundation@glowwithnora.org</p>
    <p class="site-url">www.glowwithnora.org</p>
  </article>

  <article class="poster poster--cause">
    <svg class="poster__art" viewBox="0 0 291 410">
      <rect class="photo-hero" x="110" y="0" width="181" height="300" role="img" aria-label="Photo: child crawling through a garbage dump"/>
      <path class="yellow-sweep" d="M-4,-4 H142 C112,70 150,150 210,180 C245,198 291,205 295,215 V310 H-4Z"/>
      <path class="lower-sheet" d="M-4,320 C90,255 200,236 295,262 V414 H-4Z"/>
      <path class="ribbon-drop" d="M228,132 C208,102 192,80 192,50 A36,36 0 0 1 264,50 C264,80 248,102 228,132Z"/>
      <path class="portrait-card" role="img" aria-label="Black and white photo of a baby in a hospital bed" d="M80,300 C64,300 60,286 68,274 L100,236 C108,228 118,226 130,226 H204 C222,226 228,240 218,254 L188,290 C180,298 170,300 158,300Z"/>
      <path class="support-frame" d="M22,332 V318 H36 M90,346 V360 H76"/>
      <g><rect x="24" y="350" width="13" height="8" rx="1" fill="#e8412c"/><rect x="39" y="350" width="13" height="8" rx="1" fill="#1a3a8f"/><rect x="54" y="350" width="13" height="8" rx="1" fill="#2e8bd6"/><rect x="69" y="350" width="13" height="8" rx="1" fill="#f08a1c"/></g>
      <circle cx="210" cy="362" r="2.5" fill="#333"/><rect x="205" y="367" width="5" height="5" fill="#333"/><rect x="212" y="367" width="5" height="5" fill="#333"/>
      <path class="brand-pill" d="M140,392 H295 V414 H130 C130,400 134,392 140,392Z"/>
    </svg>
    <h2 class="headline">DONATE<br>today<br>to HELP<br>a CHILD!</h2>
    <p class="fact-label">Fact 2</p>
    <p class="fact-title">Leading Cause</p>
    <p class="fact-stat">Childhood cancer is the number 1 cause of death in children under age 15 in the US.</p>
    <p class="support-note">Show your support with a small contribution today!</p>
    <div class="brand"><span class="brand__dot"></span><p class="brand__name">Nora Whitfield<br>Childhood Cancer Foundation</p></div>
    <p class="contact-email">foundation@glowwithnora.org</p>
    <p class="site-url">www.glowwithnora.org</p>
  </article>

  <article class="poster poster--funding">
    <svg class="poster__art" viewBox="0 0 291 410">
      <rect class="photo-hero" x="110" y="0" width="181" height="300" role="img" aria-label="Illustration: cancer cells under magnification"/>
      <path class="yellow-sweep" d="M-4,-4 H142 C112,70 150,150 210,180 C245,198 291,205 295,215 V310 H-4Z"/>
      <path class="lower-sheet" d="M-4,320 C90,255 200,236 295,262 V414 H-4Z"/>
      <path class="ribbon-drop" d="M228,132 C208,102 192,80 192,50 A36,36 0 0 1 264,50 C264,80 248,102 228,132Z"/>
      <path class="portrait-card" role="img" aria-label="Black and white photo of an infant with a pacifier" d="M80,300 C64,300 60,286 68,274 L100,236 C108,228 118,226 130,226 H204 C222,226 228,240 218,254 L188,290 C180,298 170,300 158,300Z"/>
      <path class="support-frame" d="M22,332 V318 H36 M90,346 V360 H76"/>
      <g><rect x="24" y="350" width="13" height="8" rx="1" fill="#e8412c"/><rect x="39" y="350" width="13" height="8" rx="1" fill="#1a3a8f"/><rect x="54" y="350" width="13" height="8" rx="1" fill="#2e8bd6"/><rect x="69" y="350" width="13" height="8" rx="1" fill="#f08a1c"/></g>
      <circle cx="210" cy="362" r="2.5" fill="#333"/><rect x="205" y="367" width="5" height="5" fill="#333"/><rect x="212" y="367" width="5" height="5" fill="#333"/>
      <path class="brand-pill" d="M140,392 H295 V414 H130 C130,400 134,392 140,392Z"/>
    </svg>
    <h2 class="headline">DONATE<br>today<br>to HELP<br>a CHILD!</h2>
    <p class="fact-label">Fact 3</p>
    <p class="fact-title">Research Funding</p>
    <p class="fact-stat">Less than 5% of the federal cancer research budget goes to childhood cancers.</p>
    <p class="support-note">Show your support with a small contribution today!</p>
    <div class="brand"><span class="brand__dot"></span><p class="brand__name">Nora Whitfield<br>Childhood Cancer Foundation</p></div>
    <p class="contact-email">foundation@glowwithnora.org</p>
    <p class="site-url">www.glowwithnora.org</p>
  </article>

  <article class="poster poster--odds">
    <svg class="poster__art" viewBox="0 0 291 410">
      <rect class="photo-hero" x="110" y="0" width="181" height="300" role="img" aria-label="Photo: child resting in a hospital bed with oxygen"/>
      <path class="yellow-sweep" d="M-4,-4 H142 C112,70 150,150 210,180 C245,198 291,205 295,215 V310 H-4Z"/>
      <path class="lower-sheet" d="M-4,320 C90,255 200,236 295,262 V414 H-4Z"/>
      <path class="ribbon-drop" d="M228,132 C208,102 192,80 192,50 A36,36 0 0 1 264,50 C264,80 248,102 228,132Z"/>
      <path class="portrait-card" role="img" aria-label="Black and white photo of a smiling child in treatment" d="M80,300 C64,300 60,286 68,274 L100,236 C108,228 118,226 130,226 H204 C222,226 228,240 218,254 L188,290 C180,298 170,300 158,300Z"/>
      <path class="support-frame" d="M22,332 V318 H36 M90,346 V360 H76"/>
      <g><rect x="24" y="350" width="13" height="8" rx="1" fill="#e8412c"/><rect x="39" y="350" width="13" height="8" rx="1" fill="#1a3a8f"/><rect x="54" y="350" width="13" height="8" rx="1" fill="#2e8bd6"/><rect x="69" y="350" width="13" height="8" rx="1" fill="#f08a1c"/></g>
      <circle cx="210" cy="362" r="2.5" fill="#333"/><rect x="205" y="367" width="5" height="5" fill="#333"/><rect x="212" y="367" width="5" height="5" fill="#333"/>
      <path class="brand-pill" d="M140,392 H295 V414 H130 C130,400 134,392 140,392Z"/>
    </svg>
    <h2 class="headline">DONATE<br>today<br>to HELP<br>a CHILD!</h2>
    <p class="fact-label">Fact 4</p>
    <p class="fact-title">One in 330</p>
    <p class="fact-stat">One in 330 children will be diagnosed with cancer by the time they are 20.</p>
    <p class="support-note">Show your support with a small contribution today!</p>
    <div class="brand"><span class="brand__dot"></span><p class="brand__name">Nora Whitfield<br>Childhood Cancer Foundation</p></div>
    <p class="contact-email">foundation@glowwithnora.org</p>
    <p class="site-url">www.glowwithnora.org</p>
  </article>
</main>
</body>
</html>
```